Redesign projects page on UK roofing website

Hi guys,

We would like to redesign the projects page of our roofing company website; https://www.brindlecoverings.com/projects

We would like to keep the top of the page the same (up to the big image). Also the footer design should remain the same.

We would like to have some nice photos of work we have done with a little bit of writing about each project.

This site has a nice projects page layout; https://www.tmwbuild.com/projects

Something along those lines would work well for our needs.

Thanks

```html
<!DOCTYPE html>
<html lang="en">
<head>
<meta charset="utf-8">
<title>Projects – Brindle Coverings</title>
<link href="https://fonts.googleapis.com/css2?family=Outfit:wght@300;400;500;600;700&display=swap" rel="stylesheet">
<style>
:root{
  --cyan:#10a9dd;
  --navy:#0b3d6e;
  --navy-mid:#22508a;
  --pale:#afc5d6;
  --ink:#1d2b3a;
  --mist:#f2f5f8;
  --white:#ffffff;
}
*{box-sizing:border-box;margin:0;padding:0}
html,body{width:1004px;height:1200px;overflow:hidden}
body{position:relative;font-family:"Outfit",sans-serif;color:var(--ink);background:var(--white)}
.abs{position:absolute}

/* hero */
.hero{left:0;top:0;width:1004px;height:457px;background:linear-gradient(160deg,#2b2b2b 0%,#4a4a4a 45%,#6a6a6a 75%,#3b3b3b 100%)}
.brand{display:flex;align-items:center;gap:6px;color:var(--white);font-weight:600;font-size:19px;letter-spacing:-.5px}
.brand-dot{width:20px;height:20px;border-radius:50%;background:var(--cyan)}
.site-logo{left:193px;top:13px}
.nav{left:402px;top:17px;display:flex;gap:0;font-size:8.5px;color:var(--white)}
.nav a{color:inherit;text-decoration:none;position:absolute;white-space:nowrap}
.nav .active{border-bottom:1.5px solid var(--cyan);padding-bottom:2px}
.btn-quote{background:var(--cyan);color:var(--white);font-weight:600;font-size:8.5px;display:flex;align-items:center;justify-content:center}
.hero-quote{left:717px;top:12px;width:95px;height:25px}
.hero-title{left:193px;top:184px;font-size:40px;font-weight:700;line-height:46px;color:var(--white);letter-spacing:-.5px}
.hero-title span{color:var(--cyan)}
.hero-rule{left:657px;top:154px;width:1px;height:149px;background:var(--cyan)}
.hero-aside{left:671px;top:160px;width:120px;color:var(--white)}
.hero-aside h2{font-size:18px;font-weight:700;line-height:23px}
.hero-aside p{margin-top:10px;font-size:10px;font-weight:300;line-height:15.6px}

/* projects */
.projects{left:0;top:457px;width:1004px;height:462px;background:var(--mist);overflow:hidden}
.filters{left:194px;top:489px;width:146px}
.filter{height:30px;margin-bottom:5.4px;border:1px solid var(--cyan);background:var(--white);display:flex;align-items:center;gap:6px;padding-left:15px;font-size:9px;font-weight:500;color:var(--cyan)}
.filter.is-active{background:var(--cyan);color:var(--white)}
.filter i{width:22px;height:22px;border-radius:50%;background:var(--cyan);display:block;position:relative}
.filter.is-active i{background:var(--white)}
.filter i::after{content:"";position:absolute;left:7px;top:6px;width:8px;height:10px;border:1px solid var(--white);border-radius:1px}
.filter.is-active i::after{border-color:var(--cyan)}
.section-title{left:350px;top:484px;font-size:21px;font-weight:600;color:var(--navy)}
.pager{top:492px;font-size:8.5px;display:flex;align-items:center;gap:6px}
.pager.prev{left:631px;color:#a9bccc}
.pager.next{left:735px;color:var(--navy)}
.intro{left:351px;top:522px;width:352px;font-size:8px;line-height:11.4px;font-weight:300;color:var(--ink)}
.card{top:606px;height:259px;color:var(--white);overflow:hidden}
.card .photo{width:100%;height:156px}
.card h3{font-size:14.5px;font-weight:600;line-height:17px}
.card p{font-size:8px;font-weight:300;line-height:11.4px}
.card-a{left:351px;width:221px;background:var(--navy)}
.card-a .body{padding:10px 10px}
.card-b{left:587px;width:220px;background:linear-gradient(180deg,#1f4f86 0%,#2a5a91 60%,#24548b 100%);padding:12px 10px}
.card-b h4{margin-top:10px;font-size:8px;font-weight:600}
.card-b .more{margin-top:10px;font-size:8px;font-weight:600;display:flex;align-items:center;gap:5px}
.card-c{left:818px;width:186px;background:var(--pale)}
.card-c .body{padding:10px 10px}
.dots{left:352px;top:880px;display:flex;gap:4px}
.dots span{width:6px;height:6px;border-radius:50%;background:#d3dbe2}
.dots span:first-child{background:var(--cyan)}

/* review bar */
.review-bar{left:2px;top:919px;width:1002px;height:42px;background:#f1f4f7}
.review{left:205px;top:932px;display:flex;align-items:center;gap:6px;font-size:9.5px;color:#222}
.stars{display:flex;gap:1px}
.stars b{width:10px;height:10px;background:#00b67a;display:block}
.review small{font-size:7px}
.bar-quote{left:715px;top:926px;width:94px;height:25px}

/* footer */
.footer{left:0;top:961px;width:1004px;height:239px;background:var(--navy);color:var(--white)}
.fcol h5{font-size:10.5px;font-weight:600;margin-bottom:7px}
.fcol a{display:block;color:var(--white);text-decoration:none;font-size:7.5px;font-weight:300;height:22px}
.social{display:flex;align-items:center;gap:5px}
.social i{width:7px;height:7px;background:var(--white);display:block}
.fcompany{left:560px;top:990px;width:250px;font-size:7px;font-weight:300;line-height:9px}
.fcompany p{margin-top:5px}
.badges{left:560px;top:1075px;display:flex;gap:14px;align-items:center}
.badges span{display:block;background:rgba(255,255,255,.85)}
.frule{left:194px;top:1166px;width:615px;height:1px;background:rgba(255,255,255,.2)}
.copy{left:194px;top:1178px;font-size:7px;font-weight:300;color:var(--white)}
</style>
</head>
<body>

<div class="abs hero" role="img" aria-label="Black and white photo of a corrugated steel roof on an industrial unit"></div>
<div class="abs brand site-logo"><span class="brand-dot"></span>brindlecoverings</div>
<nav class="abs nav">
  <a style="left:0">Services</a>
  <a style="left:66px">Clients</a>
  <a class="active" style="left:127px">Projects</a>
  <a style="left:192px">Team</a>
  <a style="left:248px">Contact</a>
</nav>
<div class="abs btn-quote hero-quote">Get a quote</div>
<h1 class="abs hero-title">Some of our <span>latest<br>projects.</span></h1>
<div class="abs hero-rule"></div>
<div class="abs hero-aside">
  <h2>What we're working on</h2>
  <p>Keep an eye on some of the latest installs, refurbs and repairs we've carried out.</p>
</div>

<section class="abs projects">
  <svg width="1004" height="462" style="position:absolute;left:0;top:0">
    <path d="M0 0 H730 C620 40 560 110 540 200 C520 300 470 380 457 462 H0 Z" fill="#ffffff"/>
  </svg>
</section>

<div class="abs filters">
  <div class="filter"><i></i>All</div>
  <div class="filter is-active"><i></i>Single Ply</div>
  <div class="filter"><i></i>Liquid Roofing</div>
  <div class="filter"><i></i>Steel Roofing</div>
  <div class="filter"><i></i>Asphalt</div>
</div>

<h2 class="abs section-title">Single Ply</h2>
<div class="abs pager prev">
  <svg width="18" height="6"><path d="M18 3H1M4 0.5 1 3 4 5.5" stroke="#a9bccc" fill="none" stroke-width="0.8"/></svg>Previous Project
</div>
<div class="abs pager next">Next Project
  <svg width="18" height="6"><path d="M0 3H17M14 0.5 17 3 14 5.5" stroke="#0b3d6e" fill="none" stroke-width="0.8"/></svg>
</div>
<p class="abs intro">Single ply is one of the most popular flat roofing materials in today's market due to its lightweight and durable design. Single Ply is commonly used on large commercial buildings such as Hospitals, Schools and Universities thanks to the speed at which it can be installed. We install a variety of single ply systems including Duraflex-T, Corvane Armourflex and Tessel Flag systems.</p>

<article class="abs card card-a">
  <div class="photo" role="img" aria-label="Photo of a wet grey single ply flat roof with ducting under a cloudy sky" style="background:linear-gradient(180deg,#cfd2d4 0%,#9a9ea2 40%,#5e6266 70%,#7c8084 100%)"></div>
  <div class="body">
    <h3>Harwick University,<br>Colchester</h3>
    <p style="margin-top:14px">Type: Single-ply (Armourflex)<br>Roof Size: 2300m2<br>Date of Completion: September, 2020</p>
  </div>
</article>

<article class="abs card card-b">
  <h3>Vale District<br>Council, Uxbridge</h3>
  <p style="margin-top:11px">Type: Single-ply (Duraflex-T S)<br>Roof Size: 300m2<br>Date of Completion: March, 2020</p>
  <h4>Contract Description</h4>
  <p>The client approached Brindle to carry out a survey of their existing flat roof coverings which were leaking in numerous places. Upon inspection our engineers quickly discovered the roofs were at end of life and required replacement. Brindle replaced all of the roofs with a new Duraflex-T single ply membrane with a 20 year manufacturer backed warranty.</p>
  <div class="more">Get In Touch Know More
    <svg width="18" height="6"><path d="M0 3H17M14 0.5 17 3 14 5.5" stroke="#fff" fill="none" stroke-width="0.8"/></svg>
  </div>
</article>

<article class="abs card card-c">
  <div class="photo" role="img" aria-label="Faded photo of a residential flat roof with houses and trees behind" style="background:linear-gradient(180deg,#c9cfd2 0%,#b7bec2 50%,#e6ebee 75%,#dfe5e8 100%)"></div>
  <div class="body">
    <h3>Private, Watford</h3>
    <p style="margin-top:14px">Type: Single-ply (Duraflex-T S)<br>Roof Size: 120m2<br>Date of Completion: February, 2020</p>
  </div>
</article>

<div class="abs dots"><span></span><span></span></div>

<div class="abs review-bar"></div>
<div class="abs review">Excellent
  <span class="stars"><b></b><b></b><b></b><b></b><b></b></span>
  <small>39 reviews on</small><strong style="font-size:7.5px">ReviewHub</strong>
</div>
<div class="abs btn-quote bar-quote">Get a quote</div>

<footer class="abs footer"></footer>
<div class="abs fcol" style="left:194px;top:990px">
  <h5>Overview</h5>
  <a>Services</a><a>Clients</a><a>Projects</a><a>Team</a><a>Contact</a>
</div>
<div class="abs fcol" style="left:297px;top:990px">
  <h5>Services</h5>
  <a>Asbestos roof removal</a><a>Steel cladding</a><a>Liquid waterproofing</a><a>Mastic asphalt roofing</a><a>Single ply roofing</a><a>Roof repairs</a><a>Emergency roof repairs</a>
</div>
<div class="abs fcol" style="left:406px;top:990px">
  <h5>Legal</h5>
  <a>Terms of service</a>
  <h5 style="margin-top:4px">Follow us</h5>
  <a class="social"><i></i>Linkwork</a>
  <a class="social"><i></i>Snapgram</a>
</div>
<div class="abs brand" style="left:560px;top:990px"><span class="brand-dot"></span>brindlecoverings</div>
<div class="abs fcompany" style="top:1018px">
  <p>Brindle Coverings Ltd is registered in England as a private limited company.</p>
  <p>Registration No: 04471829</p>
  <p>Registered Office: Unit 14 Marlow Barn, Hatchett Lane, Ashdon, Saffron Walden CB10 2PX</p>
</div>
<div class="abs badges">
  <span style="width:64px;height:22px"></span>
  <span style="width:56px;height:28px"></span>
  <span style="width:36px;height:36px;border-radius:50%"></span>
  <span style="width:66px;height:28px"></span>
</div>
<div class="abs frule"></div>
<div class="abs copy">© Copyright Brindle Coverings Ltd 2023 | All rights reserved.</div>

</body>
</html>
```